Business Card Design - Photographer

I am a landscape photographer and I require a business card design. 

I require two designs:
1)  a double sided business card
 and
b)  a single sided business card 

The single sided design can either be the same as the double sided (with just one side having all the information)....or it can be an entire new design. Its up to you.

My corporate colours are (CMYK):

Blue   69, 32, 0, 0
Grey  72,  64,  47,  31
Green  32,  2,  91,  0
Yellow   0, 19, 92, 0
Orange  0, 39, 75, 0

Colour space in final file should be in CMYK.

The details that need to be included on the card:

- Use the provided Logo
- Name: Lukas Wendrovski
- Email:   sales@vistaplume.com.au
- Website:    vistaplume.com.au
- Twitter:    twitter.com/vistaplume
- Facebook:   facebook.com/vistaplume
- Mobile  0415 309 662

Please use the attached template to design the logo to the specified size, including the marked bleed lines. I have also attached my logo in PNG (transparent background) and ai format for you to use.

The final file should be:
- Photoshop version with layers so I can edit the name/text etc. All non vector files should be high resolution at 1039 x 697 pixels at 300 dpi.

I also require a file as:
- Vector based PDF

Anyway questions please contact me.

Thank you

Industry/Entity Type

Landscape

Logo styles of interest
Pictorial/Combination Logo
Abstract Logo
Wordmark Logo
Lettermark Logo
Requirements
Must have
• The details that need to be included on the card:

- Use the provided Logo
- Name: Lukas Wendrovski
- Email: sales@vistaplume.com.au
- Website: vistaplume.com.au
- Twitter: twitter.com/vistaplume
- Facebook: facebook.com/vistaplume
- Mobile 0415 309 662

```html
<!DOCTYPE html>
<html lang="en">
<head>
<meta charset="utf-8">
<title>Vista Plume — Business Cards</title>
<link rel="stylesheet" href="https://fonts.googleapis.com/css2?family=Lato:wght@400;700&display=swap">
<style>
  :root {
    --backdrop: #1b1b1b;
    --card-light: #f1f1ef;
    --card-dark: #1f1e1e;
    --ink: #3c3c3c;
    --ink-soft: #5e5e5e;
    --brand-grey: #3d4452;
    --brand-blue: #2f7dbd;
    --brand-green: #9cc43a;
    --brand-yellow: #f6c21c;
    --brand-orange: #f39a45;
    --leaf-faint: #dedede;
  }
  * { margin: 0; padding: 0; box-sizing: border-box; }
  html, body { width: 1200px; height: 500px; overflow: hidden; }
  body {
    background: var(--backdrop);
    font-family: "Lato", Arial, sans-serif;
    position: relative;
  }
  .card {
    position: absolute;
    top: 110px;
    width: 493px;
    height: 280px;
    overflow: hidden;
  }
  /* Front */
  .card-front {
    left: 100px;
    background: var(--card-light);
    border-radius: 12px 48px 12px 12px;
  }
  .front-pattern {
    position: absolute;
    left: 0; top: 0;
    width: 150px; height: 110px;
    background: radial-gradient(ellipse at 30% 35%, var(--leaf-faint), rgba(241,241,239,0) 70%);
  }
  .brand-lockup {
    position: absolute;
    right: 22px;
    top: 46px;
    display: flex;
    align-items: center;
    gap: 10px;
  }
  .brand-dot {
    width: 26px; height: 26px;
    border-radius: 50%;
    background: var(--brand-grey);
  }
  .brand-name {
    font-size: 22px;
    font-weight: 400;
    letter-spacing: 1px;
    color: var(--brand-grey);
    text-transform: uppercase;
  }
  .holder-name {
    position: absolute;
    left: 21px; top: 160px;
    font-size: 13px;
    font-weight: 700;
    color: var(--ink);
  }
  .contact {
    position: absolute;
    left: 21px; top: 188px;
    font-size: 13px;
    line-height: 17px;
    color: var(--ink-soft);
  }
  .socials {
    position: absolute;
    left: 21px; top: 244px;
    display: flex;
    gap: 16px;
    font-size: 12px;
    color: var(--ink-soft);
  }
  .social { display: flex; align-items: center; gap: 5px; }
  .social-square {
    width: 10px; height: 10px;
    border-radius: 2px;
    background: var(--brand-blue);
  }
  .social-square.alt { background: #2e4f8f; }
  .front-web {
    position: absolute;
    right: 8px; top: 242px;
    font-size: 13px;
    color: var(--brand-blue);
  }
  /* Back */
  .card-back {
    left: 607px;
    background: var(--card-dark);
    border-radius: 48px 12px 12px 12px;
  }
  .back-band {
    position: absolute;
    right: 0; top: 0;
    width: 152px; height: 100%;
    background: var(--card-light);
  }
  .emblem-area {
    position: absolute;
    left: 198px; top: 25px;
    width: 285px; height: 250px;
    border-radius: 8px;
    background: linear-gradient(90deg, rgba(255,255,255,0.18) 0%, rgba(255,255,255,0.28) 45%, rgba(246,194,28,0.35) 70%, rgba(47,125,189,0.35) 100%);
  }
  .back-web {
    position: absolute;
    left: 21px; top: 243px;
    font-size: 15px;
    color: var(--brand-yellow);
  }
</style>
</head>
<body>
  <section class="card card-front" aria-label="Card front">
    <div class="front-pattern" role="img" aria-label="Faint leaf pattern"></div>
    <div class="brand-lockup">
      <span class="brand-dot"></span>
      <span class="brand-name">Vista Plume</span>
    </div>
    <p class="holder-name">Lukas Wendrovski</p>
    <p class="contact">sales@vistaplume.com.au<br>M. 0415 309 662</p>
    <div class="socials">
      <span class="social"><span class="social-square"></span>vistaplume</span>
      <span class="social"><span class="social-square alt"></span>vistaplume</span>
    </div>
    <p class="front-web">www.vistaplume.com.au</p>
  </section>

  <section class="card card-back" aria-label="Card back">
    <div class="back-band"></div>
    <div class="emblem-area" role="img" aria-label="Large brand emblem area"></div>
    <p class="back-web">www.vistaplume.com.au</p>
  </section>
</body>
</html>
```